Company Flyer for Electric boating company

I am looking for a company flyer which we can hand over to boat owners in the Netherlands (Amsterdam area). Our core business is to rebuild every boat (from 4 to 10 meters) into an electrically propelled boat. We are taking out diesels and replace them with a high quality electrical motor, inboard varying from 30 till 80 pk (hp). And outboard from 1pk (hp) till 200pk. We are the best, not the cheapest, not the most expensive. We only work with the best materials. The flyer has to be sort of in line with our website and branding.

Major advantages of electric boating are:
- completely silent
- no fumes, smells or smoke
- cheap to operate
- environmentally friendly
- obliged in more and more areas
- no maintenance
- more enjoyable

The flyer should be A5 format. Since all the text has to be in Dutch I expect only the graphical design and layout for advantages, process, pricing and contact details etc.

Target Market(s)

Boat owners in the Netherlands

Font styles to use
Sans Serif

Colors
9bcb3c
add136
cadf82
0555a3
3176b5
85acd3
e0ebf3

Requirements
Must have
• Clean design, in line with website: www.volta-kade.nl
Nice to have
• icons for advantages, boating etc

2 sides
Should not have
• Steering wheel...

```html
<!DOCTYPE html>
<html lang="en">
<head>
<meta charset="utf-8">
<title>Volta-Kade – Advantages of electric boating</title>
<link rel="stylesheet" href="https://fonts.googleapis.com/css2?family=Bebas+Neue&family=Oswald:wght@200;300&family=Lato:wght@400;700&family=Montserrat:wght@700;800&display=swap">
<style>
  :root {
    --navy: #272b3e;
    --navy-deep: #1f2233;
    --green: #7dbb1c;
    --green-dark: #5f9412;
    --white: #ffffff;
    --mist-1: #e9eaec;
    --mist-2: #c9cbcf;
    --water-1: #d9a27a;
    --water-2: #4f5a66;
  }
  * { box-sizing: border-box; margin: 0; padding: 0; }
  html, body { width: 839px; height: 1200px; overflow: hidden; background: var(--white); }
  .flyer { position: relative; width: 839px; height: 1200px; overflow: hidden;
    background: linear-gradient(180deg, var(--mist-2) 0%, var(--mist-1) 55%, #d7d8db 100%); font-family: "Lato", sans-serif; }
  .backdrop { position: absolute; inset: 0; }
  .top-bar { position: absolute; left: 0; top: 0; width: 100%; height: 15px; background: var(--green); }

  .brand-dot { position: absolute; left: 40px; top: 30px; width: 150px; height: 150px; border-radius: 50%; background: var(--white); }
  .brand-name { position: absolute; left: 226px; top: 60px; font-family: "Bebas Neue", sans-serif; font-size: 88px; line-height: 80px; color: var(--green); letter-spacing: 1px; }

  .headline { text-transform: uppercase; font-weight: normal; }
  .headline span { position: absolute; left: 40px; display: block; white-space: nowrap; transform-origin: left center; }
  .hl-major { top: 212px; font-family: "Bebas Neue", sans-serif; font-size: 172px; line-height: 150px; color: var(--white); }
  .hl-advantages { top: 360px; font-family: "Oswald", sans-serif; font-weight: 200; font-size: 66px; line-height: 70px; color: var(--green); letter-spacing: -1px; transform: scaleX(0.86); }
  .hl-electric { top: 430px; font-family: "Bebas Neue", sans-serif; font-size: 102px; line-height: 92px; color: var(--green); }
  .hl-boating { top: 505px; font-family: "Oswald", sans-serif; font-weight: 200; font-size: 60px; line-height: 72px; color: var(--white); letter-spacing: -1px; transform: scaleX(0.92); }

  .photo { position: absolute; border-radius: 50%; border: 5px solid var(--green); }
  .photo-harbour { left: 606px; top: 75px; width: 188px; height: 188px; background: linear-gradient(180deg, #6e7378 0%, #3d4247 100%); }
  .photo-sunset { left: 400px; top: 260px; width: 406px; height: 406px; background: radial-gradient(circle at 30% 25%, var(--water-1) 0%, #8b6e5e 40%, var(--water-2) 100%); }
  .photo-city { left: 299px; top: 557px; width: 236px; height: 236px; background: linear-gradient(180deg, #bcc7cf 0%, #b7c2c9 32%, #2f6a72 40%, #1f4a55 100%); }

  .advantages { position: absolute; left: 29px; top: 821px; width: 787px; display: grid; grid-template-columns: repeat(3, 255px); column-gap: 11px; row-gap: 30px; list-style: none; }
  .advantage { height: 48px; border-radius: 15px; background: var(--navy); color: var(--white); font-size: 16.5px; display: flex; align-items: center; justify-content: center; }
  .advantage.wide { grid-column: 1 / -1; }

  .contact-band { position: absolute; left: 0; top: 1089px; width: 100%; height: 111px; background: var(--navy); }
  .contact { position: absolute; left: 63px; top: 1065px; width: 713px; height: 135px; background: var(--green); text-align: center; color: var(--navy-deep); }
  .fold { position: absolute; top: 1065px; width: 0; height: 0; border-bottom: 22px solid var(--green-dark); }
  .fold-left { left: 40px; border-left: 23px solid transparent; }
  .fold-right { left: 776px; border-right: 23px solid transparent; }
  .contact-title { font-family: "Montserrat", sans-serif; font-weight: 800; font-size: 23px; margin-top: 12px; letter-spacing: 0.2px; }
  .contact-name { font-weight: 700; font-size: 15.5px; margin-top: 3px; }
  .contact-address { font-size: 16.5px; margin-top: 2px; }
  .contact-row { display: flex; justify-content: center; gap: 16px; margin-top: 10px; font-family: "Montserrat", sans-serif; font-weight: 700; font-size: 15px; }
  .contact-item { display: flex; align-items: center; gap: 7px; white-space: nowrap; }
  .icon { width: 22px; height: 22px; border-radius: 50%; background: var(--navy-deep); display: flex; align-items: center; justify-content: center; }
  .icon svg { width: 12px; height: 12px; fill: var(--white); }
</style>
</head>
<body>
<main class="flyer">
  <svg class="backdrop" width="839" height="1200" viewBox="0 0 839 1200" aria-hidden="true">
    <path d="M0 0 H839 V425 C760 470 640 520 560 600 C440 700 260 670 0 625 Z" fill="var(--navy)"/>
    <circle cx="603" cy="463" r="232" fill="none" stroke="#ffffff" stroke-width="1.5"/>
    <circle cx="609" cy="470" r="222" fill="none" stroke="#ffffff" stroke-width="1.5"/>
  </svg>
  <div class="top-bar"></div>

  <header class="brand">
    <span class="brand-dot"></span>
    <span class="brand-name">VOLTA-KADE</span>
  </header>

  <h1 class="headline">
    <span class="hl-major">Major</span>
    <span class="hl-advantages">Advantages of</span>
    <span class="hl-electric">Electric</span>
    <span class="hl-boating">Boating are</span>
  </h1>

  <div class="photo photo-harbour" role="img" aria-label="Photo of a grey electric sloop moored in a harbour"></div>
  <div class="photo photo-sunset" role="img" aria-label="Photo of a white electric tender cruising on the water at sunset"></div>
  <div class="photo photo-city" role="img" aria-label="Photo of an electric boat with outboard motor in front of a city skyline"></div>

  <ul class="advantages">
    <li class="advantage">Completely silent</li>
    <li class="advantage">No fumes, smells or smoke</li>
    <li class="advantage">Cheap to operate</li>
    <li class="advantage">Environmentally friendly</li>
    <li class="advantage">Obliged in more and more areas</li>
    <li class="advantage">No maintenance</li>
    <li class="advantage wide">More enjoyable</li>
  </ul>

  <div class="contact-band"></div>
  <span class="fold fold-left"></span>
  <span class="fold fold-right"></span>
  <footer class="contact">
    <h2 class="contact-title">KOM IN CONTACT MET ONS</h2>
    <p class="contact-name">Volta-Kade</p>
    <p class="contact-address">Havenkade 42 1021AB Amsterdam (Noord) Nederland</p>
    <div class="contact-row">
      <span class="contact-item"><span class="icon"><svg viewBox="0 0 24 24"><path d="M6.6 10.8a15.1 15.1 0 0 0 6.6 6.6l2.2-2.2c.3-.3.7-.4 1-.2 1.1.4 2.3.6 3.6.6.6 0 1 .4 1 1V20c0 .6-.4 1-1 1A17 17 0 0 1 3 4c0-.6.4-1 1-1h3.5c.6 0 1 .4 1 1 0 1.3.2 2.5.6 3.6.1.3 0 .7-.2 1z"/></svg></span>+31 6 12 345 678</span>
      <span class="contact-item"><span class="icon"><svg viewBox="0 0 24 24"><path d="M2 5h20v14H2z M2 5l10 8 10-8" fill="none" stroke="#fff" stroke-width="2.4"/></svg></span>info@volta-kade.nl</span>
      <span class="contact-item"><span class="icon"><svg viewBox="0 0 24 24"><path d="M12 2 2 7v2h20V7z M4 11h3v7H4z M10.5 11h3v7h-3z M17 11h3v7h-3z M2 20h20v2H2z"/></svg></span>NL00BANK0123456789</span>
      <span class="contact-item"><span class="icon"><svg viewBox="0 0 24 24"><path d="M6 2h12v20H6z M9 6h6v2H9z M9 10h6v2H9z M9 14h6v2H9z" fill-rule="evenodd"/></svg></span>12345678</span>
    </div>
  </footer>
</main>
</body>
</html>
```